Tandrel needs stationery design

We need desings for presentation cards and letter head for our company. It would be better that the letterhead uses our logo with white background and the presentation card the logo with the black background for the back of the card and the text (name, phone

Colors
0455a3
ec1f27
000000

Requirements
Must have
• Use company logo and colors

```html
<!DOCTYPE html>
<html lang="en">
<head>
<meta charset="utf-8">
<title>Tandrel Letterhead</title>
<link href="https://fonts.googleapis.com/css2?family=Jost:wght@400;500&family=Michroma&display=swap" rel="stylesheet">
<style>
  :root {
    --brand-blue: #0455a3;
    --brand-red: #ec1f27;
    --brand-black: #000000;
    --paper: #ffffff;
    --backdrop: #e9e9eb;
    --body-text: #6f7f99;
  }
  * { margin: 0; padding: 0; box-sizing: border-box; }
  html, body {
    width: 1200px;
    height: 1200px;
    overflow: hidden;
    background: var(--backdrop);
  }
  .letterhead {
    position: absolute;
    left: 195px;
    top: 28px;
    width: 810px;
    height: 1144px;
    background: var(--paper);
    overflow: hidden;
    font-family: "Jost", sans-serif;
  }
  .letterhead__shapes {
    position: absolute;
    inset: 0;
  }
  .brand-name {
    position: absolute;
    left: 63px;
    top: 50px;
    font-family: "Jost", sans-serif;
    font-weight: 400;
    font-size: 54px;
    letter-spacing: 3px;
    line-height: 60px;
    color: var(--brand-black);
  }
  .brand-tag {
    position: absolute;
    display: flex;
    align-items: center;
    gap: 6px;
    font-family: "Jost", sans-serif;
    font-weight: 500;
    font-size: 15px;
    letter-spacing: 1px;
    color: var(--brand-blue);
  }
  .brand-tag__square {
    width: 12px;
    height: 12px;
    background: var(--brand-red);
  }
  .brand-tag--top { right: 16px; top: 38px; }
  .brand-tag--bottom { left: 18px; top: 1082px; }
  .letter-body {
    position: absolute;
    left: 63px;
    top: 303px;
    width: 706px;
    font-size: 17.5px;
    line-height: 24.5px;
    color: var(--body-text);
    letter-spacing: 0.3px;
  }
  .letter-body p { margin-bottom: 24px; }
  .letter-body p:nth-child(n+3) { margin-bottom: 22px; }
  .website {
    position: absolute;
    right: 44px;
    top: 990px;
    font-family: "Michroma", sans-serif;
    font-size: 14px;
    letter-spacing: 2.5px;
    color: var(--brand-blue);
  }
  .contact {
    position: absolute;
    right: 44px;
    top: 1070px;
    font-family: "Michroma", sans-serif;
    font-size: 12.5px;
    letter-spacing: 2px;
    color: var(--paper);
  }
  .contact__row {
    display: flex;
    align-items: center;
    justify-content: flex-end;
    gap: 12px;
    height: 29px;
  }
  .contact__icon { width: 22px; height: 18px; }
</style>
</head>
<body>
  <div class="letterhead">
    <svg class="letterhead__shapes" width="810" height="1144" viewBox="0 0 810 1144">
      <path d="M0,0 H662 C648,105 588,176 498,176 H0 Z" fill="var(--brand-red)"/>
      <path d="M0,182 H520 C612,182 682,100 696,0" fill="none" stroke="var(--brand-blue)" stroke-width="7"/>
      <path d="M165,1144 C200,1068 262,1028 342,1028 H810 V1144 Z" fill="var(--brand-red)"/>
      <path d="M128,1144 C166,1060 232,1019 322,1019 H810" fill="none" stroke="var(--brand-blue)" stroke-width="6"/>
    </svg>

    <div class="brand-name">TANDREL</div>
    <div class="brand-tag brand-tag--top"><span class="brand-tag__square"></span>TANDREL</div>
    <div class="brand-tag brand-tag--bottom"><span class="brand-tag__square"></span>TANDREL</div>

    <div class="letter-body">
      <p>Lorem ipsum dolor sit amet, consectetur adipiscing elit. Fusce dignissim pretium consectetur. Curabitur tempor posuere massa in varius. Pellentesque viverra nibh eu vehicula mattis. Nullam porta facilisis justo, a feugiat dolor sodales sed. Vestibulum neque nisi, elementum tincidunt metus sit amet, egestas bibendum enim. Aenean a blandit elit, vel rutrum mi. Nunc dapibus turpis sed massa aliquet tincidunt.</p>
      <p>Pellentesque id neque ligula. Nullam posuere, ligula a mattis posuere, lacus nisl adipiscing nunc, eu congue justo est ut diam. Nam quam nibh, dignissim non consequat in, semper eget purus. Nulla arcu sapien, viverra vitae metus tempor, congue ornare diam.</p>
      <p>Pellentesque vel nibh tempus, ullamcorper tortor sed, bibendum augue. Phasellus sollicitudin justo et quam aliquam sollicitudin. Sed eget nibh mollis, mattis sem et, viverra nulla.</p>
      <p>Pellentesque vel nibh tempus, ullamcorper tortor sed, bibendum augue. Phasellus sollicitudin justo et quam aliquam sollicitudin. Sed eget nibh mollis, mattis sem et, viverra nulla.</p>
      <p>Pellentesque vel nibh tempus, ullamcorper tortor sed, bibendum augue. Phasellus sollicitudin justo et quam aliquam sollicitudin. Sed eget nibh mollis, mattis sem et, viverra nulla.</p>
    </div>

    <div class="website">WWW.TANDREL.COM</div>

    <div class="contact">
      <div class="contact__row">
        <svg class="contact__icon" viewBox="0 0 22 18" aria-hidden="true">
          <rect x="1" y="2" width="20" height="14" fill="none" stroke="#fff" stroke-width="2"/>
          <path d="M1,2 L11,10 L21,2" fill="none" stroke="#fff" stroke-width="2"/>
        </svg>
        <span>HELLO@TANDREL.COM</span>
      </div>
      <div class="contact__row">
        <svg class="contact__icon" viewBox="0 0 22 18" aria-hidden="true">
          <path d="M5,1 L8,1 L9,5 L7,7 C8,10 10,12 13,13 L15,11 L19,12 L19,15 C19,16 18,17 17,17 C9,17 3,10 3,3 C3,2 4,1 5,1 Z" fill="#fff"/>
        </svg>
        <span>+00 5550 1234 678</span>
      </div>
    </div>
  </div>
</body>
</html>
```